Business Card Design

It's an investment advisory service for individuals with all there investment needs. Also financial consulting to businesses and governmental agencies on retirement plans etc. It's personalized not commoditized help. Should show strength, knowledge and money orientation.
Updates

Reason: Will be out of town setting up office.

Reason: waiting for the 2/3rds of group to vote

Reason: only half the votes are in, I'm calling and getting verbals, but at this time we are down to 2 designs.

Industry/Entity Type

Investment

Contact Information for Business Card

B. Rel K. Financial Consulting and Wealth Management, Desmond Wick Harlow, 5172 Paseo Loma Verde Crest, San Diego, CA 92131-4817, Registered Investment Advisor

Requirements
Nice to have
• Something money oriented

```html
<!DOCTYPE html>
<html lang="en">
<head>
<meta charset="utf-8">
<title>B. Rel K. Business Card</title>
<link rel="stylesheet" href="https://fonts.googleapis.com/css2?family=Ubuntu:wght@400;500;700&display=swap">
<style>
  :root {
    --page-bg: #e9e6e1;
    --card-white: #f4f4f4;
    --brand-green: #0fa650;
    --green-light: #14b35c;
    --green-dark: #07873f;
    --text-grey: #6e6e6e;
    --money-tone: #dfe3d8;
    --white: #ffffff;
  }
  * { box-sizing: border-box; margin: 0; padding: 0; }
  html, body { width: 1200px; height: 1000px; overflow: hidden; }
  body {
    background: var(--page-bg);
    font-family: "Ubuntu", sans-serif;
    position: relative;
  }
  .card {
    position: absolute;
    left: 100px; top: 207px;
    width: 1000px; height: 586px;
    display: flex;
    box-shadow: 0 10px 30px rgba(0,0,0,0.18);
  }
  .card-front-brand {
    width: 492px; height: 100%;
    background: var(--card-white);
    position: relative;
  }
  .money-backdrop {
    position: absolute;
    right: 0; top: 120px;
    width: 240px; height: 330px;
    background: radial-gradient(ellipse at 60% 45%, var(--money-tone) 0%, rgba(223,227,216,0.5) 45%, rgba(244,244,244,0) 75%);
  }
  .brand-block {
    position: absolute;
    left: 0; right: 0; top: 155px;
    display: flex; flex-direction: column; align-items: center;
  }
  .brand-mark {
    display: flex; align-items: center; gap: 14px;
    margin-left: 40px;
  }
  .brand-square {
    width: 34px; height: 34px;
    border: 5px solid var(--brand-green);
  }
  .brand-name {
    font-weight: 700; font-size: 52px;
    color: var(--brand-green);
    letter-spacing: 1px;
  }
  .brand-tagline {
    margin-top: 64px;
    margin-left: 60px;
    font-weight: 500; font-size: 29px; line-height: 1.25;
    color: var(--text-grey);
    text-align: right;
  }
  .card-front-contact {
    flex: 1;
    background: radial-gradient(ellipse at 20% 0%, var(--green-light) 0%, var(--brand-green) 50%, var(--green-dark) 100%);
    padding: 158px 0 0 97px;
    color: var(--white);
  }
  .contact-icons { display: flex; gap: 10px; }
  .contact-icons svg { width: 48px; height: 48px; }
  .person-name {
    margin-top: 16px;
    font-weight: 700; font-size: 32px;
  }
  .credentials { margin-top: 6px; font-weight: 500; font-size: 19px; }
  .credentials sup { font-size: 12px; }
  .role { margin-top: 6px; font-weight: 500; font-size: 20px; }
  .phones { margin-top: 32px; font-weight: 500; font-size: 24px; line-height: 1.45; }
  .email { margin-top: 8px; font-weight: 500; font-size: 24px; }
</style>
</head>
<body>
  <div class="card">
    <section class="card-front-brand">
      <div class="money-backdrop" role="img" aria-label="Faded photograph of stacked banknotes"></div>
      <div class="brand-block">
        <div class="brand-mark">
          <span class="brand-square"></span>
          <span class="brand-name">B. Rel K.</span>
        </div>
        <p class="brand-tagline">Financial Consulting<br>and Wealth Management</p>
      </div>
    </section>
    <section class="card-front-contact">
      <div class="contact-icons">
        <svg viewBox="0 0 48 48" aria-label="Person">
          <circle cx="24" cy="24" r="24" fill="#fff"/>
          <circle cx="24" cy="18" r="7" fill="var(--brand-green)"/>
          <path d="M12 36c0-7 5-11 12-11s12 4 12 11z" fill="var(--brand-green)"/>
        </svg>
        <svg viewBox="0 0 48 48" aria-label="Phone">
          <circle cx="24" cy="24" r="24" fill="#fff"/>
          <path d="M16 12l5 0 2 7-3 2c1.5 3.5 4 6 7 7l2-3 7 2 0 5c-1 2-3 3-5 3-11-1-18-9-19-19 0-2 2-4 4-4z" fill="var(--brand-green)"/>
        </svg>
        <svg viewBox="0 0 48 48" aria-label="Email">
          <circle cx="24" cy="24" r="24" fill="#fff"/>
          <rect x="12" y="15" width="24" height="18" rx="2" fill="var(--brand-green)"/>
          <path d="M13 17l11 9 11-9" fill="none" stroke="#fff" stroke-width="2.2"/>
        </svg>
      </div>
      <h1 class="person-name">Desmond Wick Harlow</h1>
      <p class="credentials">MBA, RP<sup>®</sup>, CRC<sup>®</sup></p>
      <p class="role">Registered Investment Advisor</p>
      <p class="phones">858-555-0142<br>775-555-0187</p>
      <p class="email">desmond.harlow@relkmail.com</p>
    </section>
  </div>
</body>
</html>
```